Card and board game developer website, small e-commerce site

We are designing a website for Copper Lantern Otter Works. I need a homepage and a typical inside page designed.
The website navigation will be:
Home (where we'll introduce the games and the website)
Our Games (drops open into the two games)
Griffins of Morvale Keep
Tidecraft
Order Now
About Us
Contact
The header of the website will include the logo, the navigation and a link to a facebook page. The header will also include a cart icon and a link to My Account.
Then on the homepage I suggest we include a row for each game:
Griffins of Morvale Keep
This row will include a photo (or maybe a series of photos that animate into each other) and quick info about the game plus two buttons: Info and Photos (which will go to the detail page with the photo gallery), and Order Now (which will take you to the product for ordering).
Tidecraft
Your footer will contain a copyright note, plus links to:
Terms and conditions
Shipping and returns
FAQ
Contact
Account login
NOTE: the logo is the orange mokey. I've uploaded a brief with more information. The current website that we are redesigning is here https://www.copperlanternotter.example/
Please send me any questions that you have.
Target Market(s)
People interested in fun card and board games at home.
Number of Pages Required
Look and feel

```html
<!DOCTYPE html>
<html lang="en">
<head>
<meta charset="utf-8">
<title>Copper Lantern Otter Works — Home</title>
<link href="https://fonts.googleapis.com/css2?family=Poppins:ital,wght@0,400;0,500;0,600;0,700;0,800;1,600&display=swap" rel="stylesheet">
<style>
:root{
  --orange:#f07d1a;
  --orange-dark:#e06a0a;
  --peach:#fdf1e4;
  --ink:#1d1d1f;
  --muted:#5a5a5e;
  --line:#e8e2da;
  --white:#ffffff;
  --dot:#d7cfc6;
}
*{box-sizing:border-box;margin:0;padding:0}
html,body{width:1200px;height:2580px;overflow:hidden}
body{font-family:"Poppins",sans-serif;color:var(--ink);background:var(--white);position:relative}
a{color:inherit;text-decoration:none}

.site-header{position:absolute;top:0;left:0;width:1200px;height:90px;z-index:3}
.brand{position:absolute;left:36px;top:14px;display:flex;align-items:center;gap:8px;color:var(--orange);font-weight:700;font-size:13px;line-height:1.15;width:150px}
.brand-mark{width:26px;height:26px;border-radius:50%;background:var(--orange);flex:none}
.main-nav{position:absolute;left:450px;top:34px;display:flex;gap:32px;font-size:14px;font-weight:500}
.main-nav .current{color:var(--orange)}
.main-nav .has-menu::after{content:"";display:inline-block;margin-left:6px;width:6px;height:6px;border-right:1.5px solid var(--ink);border-bottom:1.5px solid var(--ink);transform:rotate(45deg) translateY(-3px)}
.header-tools{position:absolute;right:90px;top:26px;display:flex;align-items:center;gap:18px}
.icon{width:22px;height:22px}
.btn{display:inline-flex;align-items:center;justify-content:center;height:36px;padding:0 22px;border-radius:4px;font-size:13px;font-weight:500}
.btn-primary{background:var(--orange);color:var(--white)}
.btn-outline{border:1.5px solid var(--orange);color:var(--orange);background:var(--white)}

.hero{position:absolute;top:0;left:0;width:1200px;height:650px;background:var(--peach)}
.hero-copy{position:absolute;left:62px;top:160px;width:620px}
.hero-title{width:560px;font-size:42px;line-height:1.1;font-weight:800;color:var(--orange);text-transform:uppercase}
.hero-text{margin-top:16px;width:560px;font-size:15px;line-height:1.55;color:var(--muted)}
.hero-copy .btn{margin-top:24px;width:120px}
.hero-art{position:absolute;left:700px;top:40px;width:440px;height:520px;border-radius:46% 54% 40% 60%/50% 42% 58% 50%;background:radial-gradient(circle at 50% 40%,#f6c24a 0%,#f2a03a 40%,#f07d1a 75%,rgba(240,125,26,0) 76%)}

.game{position:absolute;left:0;width:1200px}
.game-one{top:650px;height:750px;background:var(--white)}
.game-two{top:1400px;height:750px;background:var(--peach)}
.burst{position:absolute;width:120px;height:120px;border-radius:50%;background:var(--orange)}
.gallery{position:absolute;width:380px;height:500px}
.card-back{position:absolute;border-radius:6px;background:#2c2b33}
.card-art{position:absolute;left:0;top:0;width:300px;height:480px;border-radius:6px;box-shadow:0 10px 24px rgba(0,0,0,.25)}
.dots{position:absolute;display:flex;gap:10px}
.dots span{width:9px;height:9px;border-radius:50%;background:var(--dot)}
.dots span:first-child{background:var(--orange)}
.game-copy{position:absolute;width:450px}
.game-title{font-size:30px;font-weight:800;color:var(--orange);text-transform:uppercase;letter-spacing:.5px;margin-bottom:12px}
.game-copy p{font-size:14.5px;line-height:1.6;color:var(--muted)}
.game-copy p b{color:var(--ink)}
.facts{list-style:none;margin-top:24px}
.facts li{position:relative;padding-left:24px;font-size:14.5px;line-height:1.6;color:var(--muted);margin-bottom:10px}
.facts li::before{content:"";position:absolute;left:2px;top:9px;width:8px;height:8px;background:var(--orange);border-radius:1px}
.actions{display:flex;gap:14px}

.site-footer{position:absolute;top:2150px;left:0;width:1200px;height:430px;background:var(--white)}
.footer-brand{position:absolute;left:100px;top:50px;width:250px}
.footer-brand .brand{position:static;width:auto}
.footer-brand p{margin-top:24px;font-size:13px;line-height:1.7;color:var(--ink)}
.footer-col{position:absolute;top:82px}
.footer-col h3{font-size:19px;font-weight:600;font-style:italic;margin-bottom:22px}
.footer-col li{list-style:none;font-size:13px;margin-bottom:22px}
.subscribe input{display:block;width:240px;height:36px;border:1px solid var(--line);border-radius:3px;padding:0 12px;font:12px "Poppins",sans-serif;color:#999}
.subscribe .btn{width:240px;margin-top:16px}
.footer-bar{position:absolute;left:100px;right:100px;top:356px;border-top:1px solid var(--line);padding-top:28px;display:flex;justify-content:space-between;font-size:13px}
.social{display:flex;gap:12px}
.social span{width:22px;height:22px;border-radius:50%;background:var(--orange)}
</style>
</head>
<body>

<section class="hero">
  <div class="hero-copy">
    <h1 class="hero-title">Discover Gaming Excellence with Copper Lantern Otter Works</h1>
    <p class="hero-text">Immerse yourself in the enchanting realms of "Griffins of Morvale Keep" and the elemental forces of "Tidecraft". Our games are crafted with passion and creativity, promising you an unparalleled gaming experience.</p>
    <a class="btn btn-primary" href="#">Order Now</a>
  </div>
  <div class="hero-art" role="img" aria-label="Orange mascot illustration of the studio in front of a sunburst"></div>
</section>

<header class="site-header">
  <a class="brand" href="#"><span class="brand-mark"></span>Copper Lantern Otter Works</a>
  <nav class="main-nav">
    <a class="current" href="#">Home</a>
    <a class="has-menu" href="#">Our Games</a>
    <a href="#">Order Now</a>
    <a href="#">About Us</a>
    <a href="#">Contact</a>
  </nav>
  <div class="header-tools">
    <svg class="icon" viewBox="0 0 24 24" fill="none" stroke="#1d1d1f" stroke-width="2"><path d="M2 3h3l2.5 12h11l2-8H6.5"/><circle cx="9" cy="20" r="1.5"/><circle cx="17" cy="20" r="1.5"/></svg>
    <svg class="icon" viewBox="0 0 24 24" fill="none" stroke="#1d1d1f" stroke-width="2"><circle cx="12" cy="12" r="10"/><circle cx="12" cy="10" r="3"/><path d="M6 19c1.5-3 4-4 6-4s4.5 1 6 4"/></svg>
    <a class="btn btn-primary" href="#">Log In</a>
  </div>
</header>

<section class="game game-one">
  <div class="burst" style="left:-30px;top:40px"></div>
  <div class="gallery" style="left:190px;top:95px">
    <div class="card-back" style="left:40px;top:20px;width:300px;height:450px;background:#3a3540"></div>
    <div class="card-back" style="left:20px;top:10px;width:300px;height:465px"></div>
    <div class="card-art" role="img" aria-label="Box art for Griffins of Morvale Keep: a castle landscape under a blue sky" style="background:linear-gradient(180deg,#3b6ea8 0%,#7fa3c7 35%,#c9a45a 65%,#4c6b35 100%)"></div>
  </div>
  <div class="dots" style="left:240px;top:620px"><span></span><span></span><span></span><span></span><span></span></div>
  <div class="game-copy" style="left:660px;top:130px">
    <h2 class="game-title">Griffins of Morvale Keep</h2>
    <p><b>Welcome</b> to Griffins of Morvale Keep, the first board game where every player is a GRIFFIN. Conquer territory and build your empire. Plunder castles and collect a huge hoard of gold. Rescue relatively attractive royalty or maybe eat them. Who knows? All we know is that everyone's a winner when the pizza's delivered!</p>
    <ul class="facts">
      <li>2 - 6 players</li>
      <li>Playtime approximately 1.5 hours.</li>
      <li>Game comes with 6 griffin packs. Additional griffin expansion packs coming soon.</li>
    </ul>
    <div class="actions" style="margin-top:74px"><a class="btn btn-primary" href="#">Order Now</a><a class="btn btn-outline" href="#">More Info</a></div>
  </div>
</section>

<section class="game game-two">
  <div class="game-copy" style="left:70px;top:195px">
    <h2 class="game-title">Tidecraft</h2>
    <p><b>Welcome</b> to Tidecraft, a fast paced card game of strategy and chance. Play your element cards (Earth, Air, Fire, Water) and wild cards (Guardian, Balance, Evolution, Genesis) wisely and be the first player to discard all of their cards and declare yourself the master of the elements.</p>
    <ul class="facts"><li>Coming to Backerhall soon.</li></ul>
    <div class="actions" style="margin-top:16px"><a class="btn btn-primary" href="#">Order Now</a><a class="btn btn-outline" href="#">More Info</a></div>
  </div>
  <div class="burst" style="left:1070px;top:530px"></div>
  <div class="gallery" style="left:620px;top:60px">
    <div class="card-back" style="left:-30px;top:40px;width:300px;height:460px"></div>
    <div class="card-back" style="left:-15px;top:20px;width:300px;height:470px;background:#3a3540"></div>
    <div class="card-art" role="img" aria-label="Tidecraft card deck box in dark teal and crimson tones" style="left:20px;width:320px;height:520px;background:linear-gradient(160deg,#1f3b3c 0%,#3d5c55 45%,#6b2a2a 100%)"></div>
  </div>
  <div class="dots" style="left:790px;top:700px"><span></span><span></span><span></span><span></span><span></span></div>
</section>

<footer class="site-footer">
  <div class="footer-brand">
    <a class="brand" href="#"><span class="brand-mark"></span>Copper Lantern Otter Works</a>
    <p>Specializing in a wide range of products, including Heating Boilers, Steam Process Boilers, Water Heaters, Water Heating Boilers, Boiler Room Accessories</p>
  </div>
  <div class="footer-col" style="left:480px">
    <h3>Helpful Links</h3>
    <ul><li>About</li><li>Our Games</li><li>Order Now</li><li>Contact</li></ul>
  </div>
  <div class="footer-col" style="left:680px">
    <h3>Information</h3>
    <ul><li>Shipping</li><li>Returns</li><li>FAQ</li></ul>
  </div>
  <div class="footer-col subscribe" style="left:880px">
    <h3>Subscribe More Info</h3>
    <input type="text" value="Enter Your Email" aria-label="Email">
    <a class="btn btn-primary" href="#">Subscribe</a>
  </div>
  <div class="footer-bar">
    <a href="#">Terms &amp; Condition</a>
    <div class="social"><span></span><span></span><span></span><span></span></div>
    <a href="#">Privacy Policy</a>
  </div>
</footer>

</body>
</html>
```